Wordpress Design for Dads Weightloss membership site

BrisketPopsHall.com

Key points
Its for Dads - so please try and make this appeal to Dad
Its for overweight men
Its a Dojo - i.e. a training school for Dads to lose weight and progress. think Karate school.

I will be launching a site to support and help Overweight Dads lose the fat. Target market is Dads 30 years + in North America, Europe.
The audience is probably well overweight but struggle to find the time due to the challenges of a demanding job and family.

The site will be a no nonsense holistic approach on how to change your lifestyle through walking/Running/Crossfit and adopting the Paleo diet. I am a 42 year old with 4 children under 7, with a demanding job in IT sales working for a global corporate. I will share my journey as a blog initially but have the intention to turn this into a business via a membership site / coaching.

I want this to be a fun yet educational but slightly tongue in cheek. Cartoon style is fine, bold and fresh. I expect a large number of users to be viewing this on their iPads or other mobile devices so please bare this in mind.

I do not want this looking like the conventional Personal Trainer web site. This looks too clinical. I am not in perfect shape myself but have proven my methods work, I am still on the journey, so want this site to be something my audience can identify with - ie I am not much different then them.

Summary
I am accepting designs concepts for my personal blog and web presence – http://www.BrisketPopsHall. The Blog, subtitled “Grit and Gut Reset for Pops”, will provide a platform upon which I wish to build a personal brand and market myself ultimately as a 1:many coach.

The successful design will balance an professional design with a bit of humour and be attractive to a male audience. The theme MUST match the concept of a oriental martial arts school. Use of Japanese imagery such as Pagodas,Zen, Bushido and Samurai is encouraged. The Web Header (Standard Header) MUST include the title and sub title and include graphics to depict a Dojo. I am open to the style and colors to be used but again please look for influences from the Far East

Technical Requirements
The design must be implementable in WordPress using “Standard Theme” Customizations to Standard Theme are allowed, but should not be extraordinary.

The design must be implementable using clean and standard html/css techniques.

The design must include a standard header that uses the Title and subtitle as discussed above. This is the key element of the design and should be your prime focus.

The design must include placeholders for advertisements on each page. Banner ad horizontal. Banner ad tower in the right .

The design must include a standard site template/shell and at least 3 internal page designs.

Designs should be submitted for (at minimum) the following pages
Home
About
Video Blog – a video surrounded by
Podcast
Primary Navigation / Pages

The Home page should include an area for Email Optin in the top right corner.
The About Page to also include the Email Optin
Each blog post should contain social actions – the ability to tweet, share, etc. . .with the click of a button.

In addition to the core content, the home page should provide a brief introduction and video.

Standard Page template to include
. This page will serve as a template for all other “standard” pages. Please include the basic elements for a website in this page. These should include:
• A minimum of 3 Headings - H1, H2, and H3
• A bulleted list
• A numbered list
• A table
• An image
• A call to action (typically an image/button)

to the public or not.

Contact
No need for a separate layout unless desired.

Other Elements
The Blog should provide quick access to the following blog “categories”:
Primal/Paleo Nutrition
Paleo Recipes
Family/Work Balance
Reducing Stress
Career Hacking
Faith and Family

The template should include prominent links to each of my social media pages:
Chirpline
Worknet
ClipStream
Chumbook
Google+
PinQuilt

The template should include a link to the blog archives

Target Market(s)

English Speaking , Male, 30+, Father, all demographics

Industry/Entity Type

Training

Requirements
Must have
• Optin area for email address on sidebar
Social icons for Pinquilt, Chumbook, You tube
Privacy, About, Terms and Conditions Navigation
Blog area
Members login - small subtle top right
First Time Visitor start Here
Nice to have
• Japanese Dojo feel to it
Should not have
• Try not to look like the many other Personal training / coaching web sites. Want to stand out from the crowd. Although this is initially a blog it will become my business. So branding is important - but in a male, not overly serious way.

```html
<!DOCTYPE html>
<html lang="en">
<head>
<meta charset="utf-8">
<title>BrisketPopsHall.com – Grit and Gut Reset for Pops</title>
<link rel="stylesheet" href="https://fonts.googleapis.com/css2?family=Cabin:wght@400;600;700&family=Cabin+Condensed:wght@400;500&family=Ubuntu:wght@400;500&family=Roboto+Slab:wght@800&display=swap">
<style>
:root{
  --page-bg:#ede6dc;
  --brand-red:#e04a2c;
  --nav-tan:#d6cfc4;
  --nav-active:#c3bbaf;
  --text-dark:#555250;
  --text-body:#5e5e5e;
  --blue-top:#3a8bd0;
  --blue-bottom:#1e5f9e;
  --page-grey:#b9b9b9;
}
*{box-sizing:border-box;margin:0;padding:0}
html,body{width:1091px;height:1200px;overflow:hidden}
body{background:var(--page-bg);position:relative;font-family:"Cabin",sans-serif;color:var(--text-body)}
.abs{position:absolute}

.top-rule{left:0;top:34px;width:1091px;height:4px;background:var(--brand-red)}

.newsletter{left:444px;top:26px;width:392px;height:57px;background:linear-gradient(#dad4cb,#c7c0b6);border:1px solid #bdb5aa;border-top:none;border-radius:0 0 4px 4px;box-shadow:0 2px 3px rgba(0,0,0,.15);display:flex;align-items:center;padding:0 12px;gap:10px}
.newsletter-label{font-family:"Ubuntu",sans-serif;font-size:15px;color:#3d3b38;letter-spacing:.5px;white-space:nowrap}
.newsletter-input{width:184px;height:25px;background:#fff;border:1px solid #cfcfcf;font-size:11px;font-style:italic;color:#a8a8a8;padding:5px 8px}
.submit-btn{width:66px;height:23px;border-radius:12px;background:linear-gradient(#6a6a6a,#2d2d2d);color:#fff;font-size:11px;font-weight:700;display:flex;align-items:center;justify-content:center;border:1px solid #999}

.social-dot{top:9px;width:55px;height:55px;border-radius:50%;background:var(--brand-red);border:2px solid #f3d3c9;display:flex;align-items:center;justify-content:center;color:#fff;font-size:10px;font-weight:600;box-shadow:0 2px 3px rgba(0,0,0,.2)}

.brand-name{left:40px;top:100px;font-family:"Cabin",sans-serif;font-weight:700;font-size:40px;color:var(--brand-red);letter-spacing:.5px}

.main-nav{left:360px;top:104px;width:679px;height:50px;background:linear-gradient(90deg,rgba(214,207,196,0) 0%,var(--nav-tan) 28%);border-radius:0 4px 4px 0;display:flex;justify-content:flex-end}
.main-nav a{font-family:"Cabin Condensed",sans-serif;font-size:18px;color:#5a554f;text-decoration:none;display:flex;align-items:center;padding:0 20px;border-left:1px solid #bdb5a9}
.main-nav a.is-active{background:var(--nav-active);color:#2f2c29;padding:0 24px}

.login-box{left:77px;top:178px;width:297px;height:220px;background:linear-gradient(#e6533a,#c93a22);border-radius:4px;box-shadow:0 3px 4px rgba(0,0,0,.25);overflow:hidden;color:#fff}
.login-badge{position:absolute;left:-30px;top:-30px;width:100px;height:100px;border-radius:50%;background:#5a1a10}
.login-badge svg{position:absolute;left:44px;top:44px}
.login-title{position:absolute;left:92px;top:20px;font-size:24px;font-weight:400;font-family:"Ubuntu",sans-serif}
.login-row{position:absolute;left:33px;display:flex;align-items:center;font-size:12px;font-style:italic}
.login-row span{width:78px}
.login-row i{display:block;width:163px;height:27px;background:#fff;border-radius:2px;border:1px solid #e9a596}
.forgot{position:absolute;left:99px;top:170px;font-size:12px;font-style:italic;text-decoration:underline}
.login-btn{position:absolute;left:207px;top:166px;width:68px;height:25px;border-radius:13px;background:linear-gradient(#676767,#2b2b2b);border:1px solid #ddd;font-size:12px;font-weight:700;display:flex;align-items:center;justify-content:center}

.visitor-banner{left:443px;top:177px;width:419px;height:73px;background:linear-gradient(var(--blue-top),var(--blue-bottom));border-radius:3px;box-shadow:0 2px 3px rgba(0,0,0,.25);display:flex;align-items:center;overflow:hidden}
.visitor-figure{width:40px;height:100%;background:linear-gradient(#2f74b4,#1c5590)}
.visitor-heading{font-family:"Roboto Slab",serif;font-weight:800;font-size:21px;color:#fff;margin-left:2px;letter-spacing:.3px}
.visitor-start{font-family:"Ubuntu",sans-serif;font-size:15px;color:#fff;margin-left:14px}
.visitor-arrow{margin-left:14px}

.scale-art{left:882px;top:153px;width:138px;height:117px;background:radial-gradient(ellipse at 50% 55%,#f6f3ef 0%,#e8e2da 60%,rgba(237,230,220,0) 100%)}
.wrestler-art{left:0;top:440px;width:404px;height:730px;background:radial-gradient(ellipse 60% 55% at 55% 42%,#d6a07c 0%,#dfb897 45%,rgba(237,230,220,0) 100%)}

.blog-panel{left:404px;top:273px;width:636px;height:873px;background:linear-gradient(#fcfcfc,#ececec);border-radius:4px;box-shadow:0 1px 4px rgba(0,0,0,.2);overflow:hidden}
.panel-head{height:52px;background:#f0f0f0;border-bottom:1px solid #e2e2e2;padding:18px 24px;font-family:"Ubuntu",sans-serif;font-size:19px;font-weight:400;color:var(--brand-red)}

.share-stack{position:absolute;left:20px;width:80px}
.share-btn{display:flex;align-items:center;margin-bottom:11px;height:18px}
.share-btn b{height:18px;border:1px solid #c8cfdb;background:linear-gradient(#fff,#e9edf4);border-radius:2px;font-size:10px;font-weight:600;color:#3b5a8e;display:flex;align-items:center;padding:0 6px}
.share-btn em{font-style:normal;font-size:10px;font-weight:700;color:#333;border:1px solid #c9c9c9;background:#fff;height:18px;padding:0 4px;margin-left:4px;display:flex;align-items:center}

.post-title{position:absolute;left:115px;font-family:"Ubuntu",sans-serif;font-size:21px;font-weight:400;color:var(--text-dark);letter-spacing:.2px}
.post-rule{position:absolute;left:115px;width:467px;border-top:1px dashed #c9c9c9}
.post-meta{position:absolute;left:115px;display:flex;font-size:11px;color:#6b6b6b;align-items:center}
.post-meta span{display:flex;align-items:center;gap:6px}
.post-art{position:absolute;left:117px;top:161px;width:491px;height:136px;border:1px solid #c9c9c9;background:linear-gradient(90deg,#8fa6c0 0%,#c23a33 22%,#e2efe8 34%,#d4e6dc 100%);display:flex;justify-content:flex-end;padding:10px 120px 0 0}
.post-art p{font-family:"Ubuntu",sans-serif;font-size:19px;color:#2d8577}
.post-body{position:absolute;left:120px;width:494px;font-size:12px;line-height:21.8px;color:var(--text-body);text-align:justify}
.continue{position:absolute;right:27px;font-family:"Ubuntu",sans-serif;font-size:14px;font-weight:500;color:#444;border-bottom:1px solid #888;line-height:15px}
.post-divider{position:absolute;left:8px;top:489px;width:614px;border-top:1px solid #d2d2d2}

.pager{position:absolute;left:0;bottom:0;width:636px;height:53px;background:linear-gradient(#dcdcdc,#cfcfcf);display:flex;align-items:center;justify-content:flex-end;padding-right:24px;gap:3px}
.pager-label{font-size:11px;color:#555;margin-right:3px}
.pager a{width:24px;height:24px;border-radius:3px;background:var(--page-grey);color:#d8d8d8;font-size:11px;display:flex;align-items:center;justify-content:center;text-decoration:none;border:1px solid #aaa}
.pager a.is-current{background:#8b8b8b;color:#fff}
.pager .dots{font-size:11px;color:#666;width:22px;text-align:center}

.copyright{left:0;top:1164px;width:1091px;text-align:center;font-size:12px;color:#5a5550}
</style>
</head>
<body>
<div class="abs top-rule"></div>

<form class="abs newsletter">
  <span class="newsletter-label">News Letter</span>
  <span class="newsletter-input">Enter your mail ID</span>
  <span class="submit-btn">SUBMIT</span>
</form>

<a class="abs social-dot" style="left:861px">Chumbook</a>
<a class="abs social-dot" style="left:921px">ClipStream</a>
<a class="abs social-dot" style="left:981px">PinQuilt</a>

<div class="abs brand-name">BrisketPopsHall.com</div>

<nav class="abs main-nav">
  <a class="is-active">Home</a>
  <a>About Us</a>
  <a>Terms and conditions</a>
  <a>Privacy policy</a>
</nav>

<div class="abs wrestler-art" role="img" aria-label="Illustrated sumo wrestler crouching in a fighting stance"></div>

<section class="abs login-box">
  <div class="login-badge">
    <svg width="36" height="40" viewBox="0 0 36 40"><circle cx="18" cy="12" r="8" fill="#e8a57a"/><path d="M2 38c0-10 7-15 16-15s16 5 16 15z" fill="#3e7ac0"/></svg>
  </div>
  <h2 class="login-title">Members login</h2>
  <div class="login-row" style="top:60px"><span>User name :</span><i></i></div>
  <div class="login-row" style="top:96px"><span>Pass word :</span><i></i></div>
  <span class="forgot">Forgot password</span>
  <span class="login-btn">LOG IN</span>
</section>

<a class="abs visitor-banner">
  <span class="visitor-figure" role="img" aria-label="Silhouette of a man"></span>
  <span class="visitor-heading">FIRST TIME VISITOR</span>
  <span class="visitor-start">START HERE</span>
  <svg class="visitor-arrow" width="32" height="32" viewBox="0 0 32 32"><circle cx="16" cy="16" r="15" fill="#e9f1f9" stroke="#8fb7de"/><path d="M13 9l7 7-7 7" fill="none" stroke="#1e5f9e" stroke-width="4" stroke-linecap="round" stroke-linejoin="round"/></svg>
</a>

<div class="abs scale-art" role="img" aria-label="Feet standing on a bathroom scale"></div>

<main class="abs blog-panel">
  <h1 class="panel-head">Blog Archieves</h1>

  <article>
    <div class="share-stack" style="top:64px">
      <div class="share-btn"><b>Like</b><em>26</em></div>
      <div class="share-btn"><b>Chirp</b><em>97</em></div>
      <div class="share-btn"><b>Share</b><em>121</em></div>
    </div>
    <h2 class="post-title" style="top:66px">Excepteur sint occaecat cupidatat non proident</h2>
    <div class="post-rule" style="top:104px"></div>
    <div class="post-meta" style="top:118px">
      <span style="width:88px"><svg width="13" height="13" viewBox="0 0 13 13"><rect x="1" y="2" width="11" height="10" fill="none" stroke="#777"/><rect x="1" y="2" width="11" height="3" fill="#777"/></svg>15 July</span>
      <span style="width:137px"><svg width="14" height="13" viewBox="0 0 14 13"><rect x="1" y="2" width="10" height="10" fill="none" stroke="#777"/><path d="M6 8l6-6" stroke="#777" stroke-width="2"/></svg>17 Comments</span>
      <span>Category : Leadership</span>
    </div>
    <div class="post-art" role="img" aria-label="Boy touching his father's belly beside a row of shrinking body silhouettes"><p>Contantry Popular</p></div>
    <p class="post-body" style="top:315px">Sed ut perspiciatis unde omnis iste natus error sit voluptatem accusantium doloremque laudantium, totam rem aperiam, eaque ipsa quae ab illo inventore veritatis et quasi architecto beatae vitae dicta sunt explicabo. Nemo enim ipsam voluptatem quia voluptas sit aspernatur aut odit aut fugit, sed quia consequuntur magni dolores eos qui ratione voluptatem sequi nesciunt. Neque porro quisquam est, qui dolorem ipsum quia dolor sit amet, consectetur, adipisci velit, sed numquam</p>
    <a class="continue" style="top:455px">Continue Reading</a>
  </article>

  <div class="post-divider"></div>

  <article>
    <div class="share-stack" style="top:506px">
      <div class="share-btn"><b>Like</b><em>26</em></div>
      <div class="share-btn"><b>Chirp</b><em>97</em></div>
      <div class="share-btn"><b>Share</b><em>121</em></div>
    </div>
    <h2 class="post-title" style="top:499px">Excepteur sint occaecat cupidatat non proident</h2>
    <div class="post-rule" style="top:537px"></div>
    <div class="post-meta" style="top:551px">
      <span style="width:88px"><svg width="13" height="13" viewBox="0 0 13 13"><rect x="1" y="2" width="11" height="10" fill="none" stroke="#777"/><rect x="1" y="2" width="11" height="3" fill="#777"/></svg>15 July</span>
      <span style="width:137px"><svg width="14" height="13" viewBox="0 0 14 13"><rect x="1" y="2" width="10" height="10" fill="none" stroke="#777"/><path d="M6 8l6-6" stroke="#777" stroke-width="2"/></svg>17 Comments</span>
      <span>Category : Leadership</span>
    </div>
    <p class="post-body" style="top:590px">Sed ut perspiciatis unde omnis iste natus error sit voluptatem accusantium doloremque laudantium, totam rem aperiam, eaque ipsa quae ab illo inventore veritatis et quasi architecto beatae vitae dicta sunt explicabo. Nemo enim ipsam voluptatem quia voluptas sit aspernatur aut odit aut fugit, sed quia consequuntur magni dolores eos qui ratione voluptatem sequi nesciunt. Neque porro quisquam est, qui dolorem ipsum quia dolor sit amet, consectetur, adipisci velit, sed numquam uis autem vel eum iure reprehenderit qui in ea voluptate velit esse quam nihil molestiae consequatur, vel illum qui dolorem eum fugiat quo voluptas nulla</p>
    <a class="continue" style="top:785px">Continue Reading</a>
  </article>

  <nav class="pager">
    <span class="pager-label">Page 1 of 32</span>
    <a class="is-current">1</a><a>2</a><a>3</a><a>4</a><a>5</a><a>6</a><a>7</a><a>8</a><a>»</a>
    <span class="dots">...</span>
    <a>»»</a>
  </nav>
</main>

<footer class="abs copyright">Copyright © 2012 weight loss program &nbsp;All rights reserved</footer>
</body>
</html>
```